Tollo is the place for Used Car Inspections

Tollo ONLY sells Used Car Inspections.

We need a website that tells that story simply.

Please be original and don't just copy my mockup. I'm not a designer.

Reason: Too few designers(<10)...too many weak designs(>80). I have subsequently revised my brief, uploaded more defined mockup and have tried to inspire some originality. I have also invited add designs, some who have declined. Any suggestions. Any suggestions?

Reason: Still waiting on original designs

Target Market(s)

Car Buyers

Industry/Entity Type

Used Car

Logo Text

Tollo

Number of Pages Required

5+ page

Font styles to use
Sans Serif

Colors
33a6d7
ffc214

Requirements
Must have
• Why Tollo?
• -Top 5 Questions
• Tollo Certified
• -Graphic detailing inspection
• How it Works
• -Graphic-- 1. Find a Location 2. Personal/Vehicle Info Form 3. Purchase
• -Get a Tollo Inspection
• Get a Tollo Inspection
• -Find a Location
• -Personal/Vehicle info Form
• -Purchase
• Become a Tollo Dealer
• -Form
• -Upload Credentials
• About Us
• Contact Us
• Term & Conditions
• Privacy
• FAQ
• Press
• Social Media
Nice to have
• Customer feedback-Quorra
Should not have
• Not sure

```html
<!DOCTYPE html>
<html lang="en">
<head>
<meta charset="utf-8">
<title>Tollo – Used Car Inspections</title>
<link href="https://fonts.googleapis.com/css2?family=Open+Sans:wght@400;600;700&display=swap" rel="stylesheet">
<style>
:root{
  --blue:#33a6d7;
  --yellow:#ffc214;
  --orange:#f39a1e;
  --dark:#2b2d2f;
  --darker:#1f2022;
  --card:#2f3b40;
  --text:#555b60;
  --muted:#9aa0a4;
  --light:#f1f2f3;
  --tile:#e9ebec;
  --white:#ffffff;
}
*{box-sizing:border-box;margin:0;padding:0}
html,body{width:682px;height:1200px;overflow:hidden}
body{font-family:"Open Sans",Arial,sans-serif;background:var(--white);color:var(--text);position:relative}
.wrap{width:492px;margin:0 auto}

.topbar{height:18px;background:var(--dark);display:flex;justify-content:flex-end;align-items:center;gap:4px;padding-right:26px}
.topbar .social{width:9px;height:9px;background:#6b7074;border-radius:2px}

.header{height:50px;display:flex;align-items:center;padding:0 26px;border-bottom:1px solid #e5e5e5}
.brand{display:flex;align-items:center;gap:6px;font-weight:700;font-size:16px;color:var(--orange);width:150px}
.brand-dot{width:12px;height:12px;border-radius:50%;background:var(--orange)}
.nav{display:flex;gap:13px;flex:1;justify-content:center}
.nav a{font-size:7.5px;color:var(--dark);text-decoration:none;font-weight:600;text-transform:uppercase}
.phone{font-size:11px;font-weight:700;color:var(--orange)}

.hero{height:262px;position:relative;background:linear-gradient(160deg,#8d969a 0%,#5e6a6e 35%,#8a2a2a 62%,#3c4042 100%)}
.hero-cta{position:absolute;left:193px;top:104px;display:flex;height:44px}
.hero-cta span{background:var(--yellow);color:var(--white);font-size:12px;font-weight:600;display:flex;align-items:center;padding:0 26px;width:262px}
.hero-cta i{width:44px;background:var(--blue);display:flex;align-items:center;justify-content:center}

.tagline{height:36px;background:var(--light);display:flex;align-items:center;justify-content:center;color:var(--orange);font-size:13px}

.features{display:grid;grid-template-columns:1fr 1fr;column-gap:20px;row-gap:8px;padding:24px 0 14px}
.feature{display:flex;gap:14px;height:88px}
.feature-icon{width:44px;height:44px;background:var(--tile);border-radius:3px;flex:none;display:flex;align-items:center;justify-content:center}
.feature h3{font-size:11px;font-weight:400;color:var(--dark);text-transform:uppercase;line-height:1.15;margin-bottom:4px}
.feature .more{font-size:6.5px;color:var(--blue);font-weight:600;display:block;margin-bottom:3px;text-transform:uppercase}
.feature p{font-size:6.5px;color:var(--muted);line-height:1.45}

.signup{height:88px;background:var(--yellow);display:flex;align-items:center;padding:0 14px 0 28px;gap:18px}
.signup h2{font-size:12px;font-weight:400;color:var(--white);flex:1}
.signup-fields{display:flex;flex-direction:column;gap:8px}
.signup-fields span{display:block;width:140px;height:16px;background:var(--white);border-radius:2px;font-size:6px;color:var(--muted);padding:4px 8px}
.signup-submit{width:40px;height:56px;background:var(--card);border-radius:2px;display:flex;flex-direction:column;align-items:center;justify-content:center;gap:3px;color:var(--white);font-size:5.5px}

.contact-cards{display:flex;gap:16px;margin-top:10px}
.contact-card{flex:1;height:94px;background:var(--card);border-radius:6px;display:flex;flex-direction:column;align-items:center;justify-content:center;gap:8px;color:var(--white);font-size:15px;text-transform:uppercase}

.testimonial{height:168px;margin-top:10px;background:var(--light);position:relative;padding:22px 24px 0 95px}
.avatar{position:absolute;left:22px;top:38px;width:60px;height:60px;border-radius:50%;background:linear-gradient(#a07b62,#5a3b2c)}
.testimonial .mark{position:absolute;left:95px;top:12px;font-size:20px;color:var(--muted);font-weight:700}
.testimonial blockquote{font-size:10px;line-height:1.55;color:var(--text);padding-top:10px}
.testimonial cite{display:block;font-style:normal;font-size:7px;margin-top:10px;color:var(--dark);font-weight:600}
.testimonial cite small{font-weight:400;color:var(--muted)}
.feature-car{position:absolute;right:18px;bottom:24px;width:110px;height:58px;border-radius:30px 30px 8px 8px;background:linear-gradient(#5fb0d8,#2e7fae)}
.dots{position:absolute;bottom:10px;left:0;right:0;display:flex;justify-content:center;gap:4px}
.dots b{width:5px;height:5px;border-radius:50%;background:#c5c9cc}
.dots b:first-child{background:var(--muted)}

.footer{position:absolute;top:1064px;left:0;width:682px;height:118px;background:var(--dark);display:flex;padding:18px 0 0 95px;gap:34px}
.footer .brand{width:118px;align-self:flex-start;margin-top:22px}
.footer h4{font-size:6.5px;color:var(--white);font-weight:600;margin-bottom:6px;text-transform:uppercase}
.footer ul{list-style:none}
.footer li{font-size:6px;color:#aab0b4;line-height:1.7}
.footer .col{width:100px}
.copyright{position:absolute;top:1182px;left:0;width:682px;height:18px;background:var(--darker);font-size:5.5px;color:#8a9094;display:flex;align-items:center;justify-content:center}
</style>
</head>
<body>

<div class="topbar">
  <span class="social"></span><span class="social"></span><span class="social"></span>
</div>

<header class="header">
  <div class="brand"><span class="brand-dot"></span>Tollo</div>
  <nav class="nav">
    <a>Home</a><a>About us</a><a>Tollo Certified</a><a>Why Tollo</a><a>FAQs</a><a>Contact us</a>
  </nav>
  <div class="phone">800-555-0142</div>
</header>

<section class="hero" role="img" aria-label="Photo of used cars lined up at an outdoor car lot">
  <a class="hero-cta"><span>GET A TOLLO INSPECTION TODAY</span><i>
    <svg width="16" height="14" viewBox="0 0 16 14"><path d="M1 7h12M8 2l5 5-5 5" stroke="#fff" stroke-width="2.4" fill="none"/></svg></i></a>
</section>

<div class="tagline">Tollo is the place for used car inspections</div>

<main class="wrap">
  <section class="features">
    <div class="feature">
      <div class="feature-icon"><svg width="20" height="26" viewBox="0 0 20 26"><path d="M10 1a8 8 0 0 0-8 8c0 6 8 16 8 16s8-10 8-16a8 8 0 0 0-8-8z" fill="#33a6d7"/><circle cx="10" cy="9" r="3" fill="#e9ebec"/></svg></div>
      <div><h3>1. Find a<br>location</h3><span class="more">How it works</span><p>Choose a certified Tollo inspection point near the seller in a few clicks.</p></div>
    </div>
    <div class="feature">
      <div class="feature-icon"><svg width="22" height="26" viewBox="0 0 22 26"><path d="M2 1h12l6 6v18H2z" fill="#33a6d7"/><path d="M6 11h10M6 15h10M6 19h7" stroke="#e9ebec" stroke-width="1.6"/></svg></div>
      <div><h3>2. Add your<br>vehicle info</h3><span class="more">How it works</span><p>Tell us about you and the car: make, model, year and the seller details.</p></div>
    </div>
    <div class="feature">
      <div class="feature-icon"><svg width="18" height="28" viewBox="0 0 18 28"><text x="9" y="23" text-anchor="middle" font-family="Open Sans, sans-serif" font-weight="700" font-size="26" fill="#33a6d7">$</text></svg></div>
      <div><h3>3. Purchase your<br>inspection</h3><span class="more">How it works</span><p>Pay one simple flat price online and we book the inspection for you.</p></div>
    </div>
    <div class="feature">
      <div class="feature-icon"><svg width="26" height="26" viewBox="0 0 26 26"><circle cx="13" cy="13" r="12" fill="#33a6d7"/><path d="M7 13l4 4 8-8" stroke="#e9ebec" stroke-width="2.6" fill="none"/></svg></div>
      <div><h3>Tollo<br>certified</h3><span class="more">Full inspection</span><p>Engine, brakes, body, tyres and electrics checked by a trusted mechanic.</p></div>
    </div>
    <div class="feature">
      <div class="feature-icon"><svg width="24" height="24" viewBox="0 0 24 24" fill="none" stroke="#33a6d7" stroke-width="3"><circle cx="10" cy="10" r="7"/><path d="M15 15l7 7"/></svg></div>
      <div><h3>Only used car<br>inspections</h3><span class="more">Why Tollo</span><p>We sell nothing else, so our only job is giving you an honest report.</p></div>
    </div>
    <div class="feature">
      <div class="feature-icon"><svg width="26" height="24" viewBox="0 0 26 24"><path d="M13 23S1 15 1 7.5A6 6 0 0 1 13 5a6 6 0 0 1 12 2.5C25 15 13 23 13 23z" fill="#33a6d7"/></svg></div>
      <div><h3>Buy with<br>confidence</h3><span class="more">Why Tollo</span><p>Know exactly what you are buying before you hand over any money.</p></div>
    </div>
  </section>

  <section class="signup">
    <h2>BECOME A TOLLO DEALER</h2>
    <div class="signup-fields"><span>Your name</span><span>Your email</span></div>
    <div class="signup-submit">
      <svg width="16" height="12" viewBox="0 0 16 12"><path d="M1 1h10v7H5l-3 3V8H1z" fill="#ffc214"/><path d="M12 4h3v6h-1v2l-2-2H7V9h5z" fill="#ffc214"/></svg>SUBMIT
    </div>
  </section>

  <section class="contact-cards">
    <div class="contact-card"><svg width="32" height="22" viewBox="0 0 32 22"><rect width="32" height="22" rx="2" fill="#ffc214"/><path d="M1 2l15 11L31 2" stroke="#2f3b40" stroke-width="2" fill="none"/></svg>Email us</div>
    <div class="contact-card"><svg width="26" height="26" viewBox="0 0 26 26"><rect width="26" height="26" rx="3" fill="#ffc214"/><path d="M8 5l3 4-2 2c1 3 3 5 6 6l2-2 4 3-2 3c-7 0-14-7-14-14z" fill="#2f3b40"/></svg>Call us</div>
    <div class="contact-card"><svg width="22" height="28" viewBox="0 0 22 28"><text x="11" y="25" text-anchor="middle" font-family="Open Sans, sans-serif" font-weight="700" font-size="30" fill="#ffc214">?</text></svg>FAQs</div>
  </section>

  <section class="testimonial">
    <div class="avatar" role="img" aria-label="Portrait photo of a customer"></div>
    <span class="mark">“</span>
    <blockquote>The Tollo inspection found a worn clutch the seller never mentioned. I negotiated the price down and bought the car knowing exactly what I was getting.</blockquote>
    <cite>Marcus Bell <small>Car Buyer, Denver</small></cite>
    <div class="feature-car" role="img" aria-label="Photo of a light blue vintage car"></div>
    <div class="dots"><b></b><b></b><b></b></div>
  </section>
</main>

<footer class="footer">
  <div class="brand"><span class="brand-dot"></span>Tollo</div>
  <div class="col"><h4>Quick links</h4><ul><li>Home</li><li>About Us</li><li>FAQ</li><li>Privacy</li><li>Contact Us</li></ul></div>
  <div class="col"><h4>Information</h4><ul><li>How it Works</li><li>Tollo Certified</li><li>Become a Dealer</li><li>Terms &amp; Conditions</li><li>Press</li></ul></div>
  <div class="col"><h4>Address</h4><ul><li>123 Harbor Lane Avenue</li><li>Springfield</li><li>Ph: 800-555-0142</li><li>E-mail: info@tollo.com</li></ul></div>
</footer>
<div class="copyright">© 2015 Tollo. All rights reserved.</div>

</body>
</html>
```